Flyer für Stadtverwaltung
Zielgruppe
Wir sind die Stadtverwaltung der Stadt Wermelskirchen,
unsere Zielgruppe sind Schüler/innen, welche demnächst ihren Abschluss machen und Interesse an einer Ausbildung oder einem dualen Studium haben.
Aber auch alle weiteren Personengruppen, die sich für eine Ausbildung oder ein duales Studium interessieren.
Aufgabenstellung
Sehr geehrtes Team von Kreavolo,
unser Flyer soll hauptsächlich Schüler/innen ansprechen,
die in näherer Zukunft ihren Abschluss machen und Interesse an einer Ausbildung oder einem dualen Studium haben.
Darf sich jedoch an jede/n richten, der/die Interesse an einer Ausbildung oder einem dualen Studium hat.
Der Flyer soll DIN A5 Format haben, ob quer oder hoch ist den Designer/innen überlassen, wir sind offen für Ideen und Vorschläge.
Was auf den Flyer muss:
1. Die folgenden Ausbildungsberufe (In exakt der vorgegebenen Schreibweise)
> unsere Ausschreibungen richten sich an Personen jeglichen Geschlechts (m/w/d) sowie an Personen mit einer Schwerbehinderung (dies sollte in irgendeiner Form auf dem Flyer deutlich werden)
- Bachelor- Studiengang Kommunaler Verwaltungsdienst
- Bachelor- Studiengang Verwaltungsinformatik
- Verwaltungsfachangestellte/r
- Straßenwärter/in
- Fachangestellte/r für Medien- und Informationsdienste
- Fachangestellte/r für Bäderbetriebe
- Fachinformatiker/in in der Fachrichtung Systemintegration
- Brandmeisteranwärter/in
- Ausbildung zum/zur Notfallsanitäter/in
- Elektroniker/in für Betriebstechnik
- PIA- Ausbildung
2. Die beigefügten Fotos
- Die Fotos dürfen gerne ergänzt, ersetzt oder vollständig weggelassen werden
- Gerne dürfen eigene Designs, Grafiken, Bilder oder sonstige Formen der Darstellung verwendet werden die der Gestaltung des Flyers dienlich sind. (Wir freuen uns auf Kreative Ideen)
- Eine Orientierung am Stil der Fotos ist ebenso nicht notwendig
Der Flyer soll die Vielfalt an beruflichen Optionen widerspiegeln, die es bei der Stadt Wermelskirchen gibt.
Zudem soll die Stadt Wermelskirchen als offener und toleranter Arbeitgeber präsentiert werden, dem seine Angestellten am Herzen liegen.
Ideen und Anregungen für den Flyer:
Die Möglichkeit:
- eine Beamtenlaufbahn einzuschlagen
- draußen zu arbeiten

```html
<!DOCTYPE html>
<html lang="de">
<head>
<meta charset="utf-8">
<title>Ausbildung und duales Studium – Flyer</title>
<link href="https://fonts.googleapis.com/css2?family=League+Gothic&family=Montserrat:wght@600;700&family=Oswald:wght@300&display=swap" rel="stylesheet">
<style>
  :root {
    --red: #f60000;
    --dark-red: #c40000;
    --yellow: #e0d300;
    --ink: #474c53;
    --white: #ffffff;
    --stage: #7f7f7f;
    --display: "League Gothic", "Oswald", sans-serif;
    --display-light: "Oswald", sans-serif;
    --body: "Montserrat", Arial, sans-serif;
  }
  * { margin: 0; padding: 0; box-sizing: border-box; }
  html, body { width: 1112px; height: 1200px; overflow: hidden; background: var(--stage); }
  .flyer {
    position: absolute; left: 61px; top: 250px;
    width: 990px; height: 699px;
    background: var(--white); overflow: hidden;
  }
  .layer { position: absolute; left: 0; top: 0; width: 990px; height: 699px; }
  .display { position: absolute; font-family: var(--display); line-height: 1; text-transform: uppercase; white-space: nowrap; }
  .headline { left: 45px; width: 370px; text-align: center; color: var(--ink); }
  .headline--lead { font-size: 64px; }
  .headline--key { font-size: 100px; color: var(--red); }
  .headline--sub { font-family: var(--display-light); font-weight: 300; font-size: 36px; letter-spacing: -1px; transform: scaleX(0.72); }
  .headline--end { font-size: 56px; color: var(--red); }
  .section-title { left: 121px; width: 366px; top: 381px; font-size: 27px; color: var(--white); text-align: center; }
  .job { position: absolute; font-family: var(--body); font-weight: 600; font-size: 13px; line-height: 16px; color: var(--ink); }
  .offer-title { left: 752px; top: 322px; font-size: 34px; color: var(--white); }
  .claim { left: 783px; width: 207px; top: 202px; font-size: 56px; line-height: 0.86; color: #2c2c2c; text-align: center; }
  .benefit { position: absolute; left: 800px; font-family: var(--body); font-weight: 700; font-size: 14px; color: var(--white); line-height: 18px; }
  .note { position: absolute; right: 45px; top: 630px; text-align: right; font-family: var(--body); font-weight: 700; font-size: 18px; line-height: 23px; color: var(--ink); }
</style>
</head>
<body>
<main class="flyer">
  <svg class="layer" viewBox="0 0 990 699">
    <defs>
      <linearGradient id="backdrop-fade" x1="0" x2="1" y1="0" y2="0">
        <stop offset="0" stop-color="#ffffff" stop-opacity="0"/>
        <stop offset="0.35" stop-color="#dfe8f1"/>
        <stop offset="1" stop-color="#e9eef3"/>
      </linearGradient>
      <linearGradient id="truck-tone" x1="0" x2="1" y1="0" y2="1">
        <stop offset="0" stop-color="#eef1f4"/>
        <stop offset="0.6" stop-color="#d9dde2"/>
        <stop offset="1" stop-color="#8a8f96"/>
      </linearGradient>
      <linearGradient id="portrait-tone" x1="0" x2="0" y1="0" y2="1">
        <stop offset="0" stop-color="#eef1f4"/>
        <stop offset="1" stop-color="#f6a273"/>
      </linearGradient>
      <linearGradient id="crew-tone" x1="0" x2="1" y1="0" y2="1">
        <stop offset="0" stop-color="#8e99b4"/>
        <stop offset="1" stop-color="#2b2f3b"/>
      </linearGradient>
      <linearGradient id="ambulance-tone" x1="0" x2="1" y1="0" y2="1">
        <stop offset="0" stop-color="#f4f4f4"/>
        <stop offset="0.5" stop-color="#f23a2a"/>
        <stop offset="1" stop-color="#b7b7b7"/>
      </linearGradient>
      <clipPath id="crew-clip"><circle cx="646" cy="348" r="78"/></clipPath>
      <clipPath id="ambulance-clip"><circle cx="646" cy="522" r="77"/></clipPath>
    </defs>

    <rect x="330" y="0" width="330" height="380" fill="url(#backdrop-fade)" role="img" aria-label="Unscharfes Foto eines städtischen Einsatzfahrzeugs als Hintergrund"/>
    <rect x="650" y="0" width="340" height="196" fill="url(#truck-tone)" role="img" aria-label="Foto: Auszubildende in Warnkleidung vor einem weißen Räumfahrzeug des Tiefbauamts"/>

    <polygon points="0,0 433,0 418,17 0,17" fill="var(--red)"/>

    <rect x="444" y="40" width="256" height="340" fill="url(#portrait-tone)" role="img" aria-label="Foto: junger Auszubildender in orangefarbener Warnjacke"/>

    <circle cx="646" cy="348" r="87" fill="var(--white)"/>
    <rect x="560" y="262" width="172" height="172" fill="url(#crew-tone)" clip-path="url(#crew-clip)" role="img" aria-label="Foto: zwei Auszubildende der Feuerwehr in dunkler Dienstkleidung"/>
    <circle cx="646" cy="522" r="81" fill="var(--white)"/>
    <rect x="565" y="441" width="162" height="162" fill="url(#ambulance-tone)" clip-path="url(#ambulance-clip)" role="img" aria-label="Foto: zwei Auszubildende an einem Rettungswagen"/>

    <rect x="46" y="383" width="75" height="4" fill="var(--yellow)"/>
    <rect x="46" y="392" width="75" height="4" fill="var(--red)"/>
    <rect x="46" y="401" width="75" height="4" fill="var(--yellow)"/>
    <rect x="487" y="383" width="88" height="4" fill="var(--yellow)"/>
    <rect x="487" y="392" width="88" height="4" fill="var(--red)"/>
    <rect x="487" y="401" width="88" height="4" fill="var(--yellow)"/>
    <polygon points="135,377 473,377 487,394 473,411 135,411 121,394" fill="var(--red)"/>

    <rect x="44" y="275" width="101" height="2.5" fill="var(--ink)"/>
    <rect x="312" y="275" width="101" height="2.5" fill="var(--ink)"/>

    <g fill="var(--red)">
      <circle cx="52" cy="431" r="5.5"/><circle cx="52" cy="479" r="5.5"/><circle cx="52" cy="527" r="5.5"/>
      <circle cx="52" cy="558" r="5.5"/><circle cx="52" cy="590" r="5.5"/><circle cx="52" cy="638" r="5.5"/>
      <circle cx="313" cy="432" r="5.5"/><circle cx="313" cy="480" r="5.5"/><circle cx="313" cy="512" r="5.5"/>
      <circle cx="313" cy="560" r="5.5"/><circle cx="313" cy="591" r="5.5"/>
    </g>
    <g fill="none" stroke="var(--white)" stroke-width="1.6" stroke-linecap="round" stroke-linejoin="round">
      <path d="M49.5 431 l2 2 l3.5 -3.5"/><path d="M49.5 479 l2 2 l3.5 -3.5"/><path d="M49.5 527 l2 2 l3.5 -3.5"/>
      <path d="M49.5 558 l2 2 l3.5 -3.5"/><path d="M49.5 590 l2 2 l3.5 -3.5"/><path d="M49.5 638 l2 2 l3.5 -3.5"/>
      <path d="M310.5 432 l2 2 l3.5 -3.5"/><path d="M310.5 480 l2 2 l3.5 -3.5"/><path d="M310.5 512 l2 2 l3.5 -3.5"/>
      <path d="M310.5 560 l2 2 l3.5 -3.5"/><path d="M310.5 591 l2 2 l3.5 -3.5"/>
    </g>

    <rect x="737" y="250" width="253" height="352" fill="var(--red)"/>
    <polygon points="737,250 760,250 783,307 990,307 990,314 772,314" fill="var(--dark-red)"/>
    <polygon points="790,195 990,195 990,307 783,307 760,250" fill="var(--yellow)"/>

    <g fill="var(--yellow)">
      <rect x="800" y="400" width="190" height="1.6"/><rect x="800" y="448" width="190" height="1.6"/>
      <rect x="800" y="495" width="190" height="1.6"/><rect x="800" y="543" width="190" height="1.6"/>
    </g>

    <g fill="var(--yellow)">
      <circle cx="771" cy="380" r="19"/><circle cx="771" cy="428" r="19"/><circle cx="771" cy="474" r="19"/>
      <circle cx="771" cy="522" r="19"/><circle cx="771" cy="570" r="19"/>
    </g>
    <g fill="none" stroke="var(--red)" stroke-width="1.5" stroke-linecap="round" stroke-linejoin="round">
      <rect x="761" y="369" width="16" height="10" rx="1" transform="rotate(-15 769 374)"/>
      <path d="M760 385 q5 -3 10 0 l6 0 q3 0 6 -3 M760 390 l14 0 l8 -5"/>
      <circle cx="782" cy="388" r="3"/>
      <path d="M764 418 h13 v20 h-13 q-3 0 -3 -3 v-14 q0 -3 3 -3 z M764 434 h13"/>
      <rect x="763" y="463" width="13" height="20" rx="1.5"/>
      <path d="M766 468 h7 M766 472 h7 M766 476 h4"/>
      <circle cx="779" cy="480" r="4"/>
      <rect x="759" y="515" width="24" height="14" rx="2"/>
      <path d="M765 522 h10 M772 519 l3 3 l-3 3"/>
      <rect x="759" y="563" width="24" height="15" rx="2"/>
      <path d="M766 563 v-3 h10 v3 M766 571 h10 M773 568 l3 3 l-3 3"/>
    </g>

    <polygon points="0,670 355,670 344,684 0,684" fill="var(--red)"/>
    <polygon points="400,616 990,616 990,699 0,699 0,684 346,684" fill="var(--yellow)"/>
  </svg>

  <div class="display headline headline--lead" style="top:50px">Willst du</div>
  <div class="display headline headline--lead" style="top:106px">Interesse an einer</div>
  <div class="display headline headline--key" style="top:163px">Ausbildung</div>
  <div class="display headline headline--sub" style="top:255px">oder einem</div>
  <div class="display headline headline--end" style="top:296px">Dualen Studium hat?</div>

  <div class="display section-title">Die folgenden Ausbildungsberufe</div>

  <div class="job" style="left:73px;top:424px">Bachelor- Studiengang<br>Kommunaler Verwaltungsdienst</div>
  <div class="job" style="left:73px;top:472px">Bachelor- Studiengang<br>Verwaltungsinformatik</div>
  <div class="job" style="left:73px;top:520px">Verwaltungsfachangestellte/r</div>
  <div class="job" style="left:73px;top:551px">Straßenwärter/in</div>
  <div class="job" style="left:73px;top:583px">Fachangestellte/r für Medien-<br>und Informationsdienste</div>
  <div class="job" style="left:73px;top:631px">Fachangestellte/r für Bäderbetriebe</div>
  <div class="job" style="left:332px;top:425px">Fachinformatiker/in in der<br>Fachrichtung Systemintegration</div>
  <div class="job" style="left:332px;top:473px">Brandmeisteranwärter/in</div>
  <div class="job" style="left:332px;top:505px">Ausbildung zum/zur<br>Notfallsanitäter/in</div>
  <div class="job" style="left:332px;top:553px">Elektroniker/in für Betriebstechnik</div>
  <div class="job" style="left:332px;top:584px">PIA- Ausbildung</div>

  <div class="display claim">Etwas zu<br>bewirken</div>
  <div class="display offer-title">Die Stadt bietet</div>

  <div class="benefit" style="top:371px">Eine faire Bezahlung</div>
  <div class="benefit" style="top:419px">Lernmittelzuschuss</div>
  <div class="benefit" style="top:465px">Büchergeld</div>
  <div class="benefit" style="top:513px">Deutschlandticket</div>
  <div class="benefit" style="top:561px">30 Tage Urlaub</div>

  <p class="note">Richten sich an Personen jeglichen Geschlechts (m/w/d)<br>sowie an Personen mit einer Schwerbehinderung</p>
</main>
</body>
</html>
```